One Thumbnail for Online Shop for SlideDeck Templates needed

We are selling SlideDeck Templates and need therefore a thumbnail for our online shop.

You can use a stock photo, mock-ups or other design elements.

Format:
squared like 500 x 500
or wide like 1280 x 720

If you want to use a title, use:

"Graphs" ---> Title
"SlideDeck template" ---> subtitle

Attachments:
- OLD: Our old thumbnail which I do not like
- Template: SlideDeck pictures which you can use ( you can also copy them if you need more than these)
- Example: Some examples I found from other shops (please do not copy them exactly, only to show what I mean)

I received lots of designs until now but many are not what I have expected

Target Market(s)

E-Commerce

Industry/Entity Type

Shop

Font styles to use
Sans Serif

Requirements
Should not have
• Do NOT re-design one of the template.png (these are only examples, I will replace them later)

```html
<!DOCTYPE html>
<html lang="en">
<head>
<meta charset="utf-8">
<title>SlideDeck Template 1</title>
<link href="https://fonts.googleapis.com/css2?family=Montserrat:wght@600&family=Arimo:wght@400;700&display=swap" rel="stylesheet">
<style>
  :root {
    --page: #ffffff;
    --wall: #474c53;
    --wall-dark: #34383e;
    --desk: #5b4332;
    --desk-dark: #3b2a1f;
    --slide: #f6f7f8;
    --ink: #222222;
    --muted: #6f6f6f;
    --bar-dark: #1d4f7e;
    --bar-light: #4a8fd6;
    --axis: #b9bcc0;
    --caption: #ffffff;
  }
  * { box-sizing: border-box; margin: 0; padding: 0; }
  html, body { width: 1200px; height: 1189px; overflow: hidden; background: var(--page); }
  .thumbnail { position: relative; width: 1200px; height: 1189px; }
  .scene-photo {
    position: absolute; left: 32px; top: 14px; width: 1138px; height: 1147px;
    background: linear-gradient(180deg, var(--wall-dark) 0%, var(--wall) 45%, #6c6a68 62%, var(--desk) 80%, var(--desk-dark) 100%);
  }
  .slide {
    position: absolute; left: 269px; top: 194px; width: 795px; height: 492px;
    background: var(--slide); font-family: "Arimo", Arial, sans-serif; color: var(--ink);
  }
  .slide-title { position: absolute; top: 12px; width: 100%; text-align: center; font-weight: 700; font-size: 31px; }
  .slide-lead { position: absolute; top: 54px; width: 100%; text-align: center; font-size: 16px; color: #333; }
  .chart { position: absolute; width: 230px; }
  .chart-title { font-weight: 700; font-size: 12px; }
  .chart-note { font-size: 7px; color: var(--muted); margin-bottom: 2px; white-space: nowrap; }
  .chart svg { display: block; width: 230px; height: 105px; }
  .notes { position: absolute; left: 586px; top: 158px; width: 196px; }
  .note { position: relative; padding-left: 20px; font-size: 10px; line-height: 1.3; color: var(--muted); margin-bottom: 34px; text-align: justify; }
  .note::before { content: ""; position: absolute; left: 4px; top: 5px; width: 5px; height: 5px; border-radius: 50%; background: var(--bar-dark); }
  .legend { position: absolute; left: 520px; top: 412px; font-size: 7px; color: var(--muted); line-height: 1.7; }
  .legend span::before { content: ""; display: inline-block; width: 6px; height: 6px; margin-right: 4px; }
  .legend .light::before { background: var(--bar-light); }
  .legend .dark::before { background: var(--bar-dark); }
  .caption {
    position: absolute; left: 180px; top: 1030px;
    font-family: "Montserrat", Arial, sans-serif; font-weight: 600; font-size: 46px;
    letter-spacing: 5px; color: var(--caption); white-space: nowrap;
  }
</style>
</head>
<body>
<div class="thumbnail">
  <div class="scene-photo" role="img" aria-label="Photo of a silver laptop on a wooden desk in front of a grey wall, with a plant at the top left"></div>

  <div class="slide">
    <h1 class="slide-title">Lorem ipsum dolor sit amet</h1>
    <p class="slide-lead">Lorem ipsum dolor sit amet, consectetuer adipiscing elit. Aenean commodo ligula eget dolor.</p>

    <div class="chart" style="left:44px;top:106px">
      <div class="chart-title">Lorem ipsum</div>
      <div class="chart-note">Lorem ipsum dolor sit amet, consectetur adipiscing elit</div>
      <svg viewBox="0 0 258 118">
        <g fill="var(--muted)" font-size="6" font-family="Arimo, sans-serif"><text x="0" y="10">140</text><text x="0" y="40">100</text><text x="4" y="70">60</text><text x="4" y="100">20</text></g>
        <line x1="20" y1="112" x2="255" y2="112" stroke="var(--axis)"/>
        <g fill="var(--bar-light)"><rect x="28" y="86" width="9" height="26"/><rect x="47" y="70" width="9" height="42"/><rect x="66" y="40" width="9" height="72"/><rect x="85" y="26" width="9" height="86"/><rect x="104" y="36" width="9" height="76"/><rect x="123" y="42" width="9" height="70"/><rect x="142" y="46" width="9" height="66"/><rect x="161" y="50" width="9" height="62"/><rect x="180" y="44" width="9" height="68"/><rect x="199" y="50" width="9" height="62"/><rect x="218" y="54" width="9" height="58"/><rect x="237" y="52" width="9" height="60"/></g>
        <g fill="var(--bar-dark)"><rect x="28" y="96" width="9" height="16"/><rect x="47" y="86" width="9" height="26"/><rect x="66" y="72" width="9" height="40"/><rect x="85" y="70" width="9" height="42"/><rect x="104" y="72" width="9" height="40"/><rect x="123" y="74" width="9" height="38"/><rect x="142" y="76" width="9" height="36"/><rect x="161" y="76" width="9" height="36"/><rect x="180" y="74" width="9" height="38"/><rect x="199" y="78" width="9" height="34"/><rect x="218" y="78" width="9" height="34"/><rect x="237" y="80" width="9" height="32"/></g>
      </svg>
    </div>

    <div class="chart" style="left:300px;top:106px">
      <div class="chart-title">Lorem ipsum</div>
      <div class="chart-note">Lorem ipsum dolor sit amet, consectetur adipiscing elit</div>
      <svg viewBox="0 0 258 118">
        <g fill="var(--muted)" font-size="6" font-family="Arimo, sans-serif"><text x="0" y="10">140</text><text x="0" y="40">100</text><text x="4" y="70">60</text><text x="4" y="100">20</text></g>
        <line x1="20" y1="112" x2="255" y2="112" stroke="var(--axis)"/>
        <g fill="var(--bar-light)"><rect x="28" y="44" width="9" height="68"/><rect x="47" y="56" width="9" height="56"/><rect x="66" y="60" width="9" height="52"/><rect x="85" y="26" width="9" height="86"/><rect x="104" y="32" width="9" height="80"/><rect x="123" y="46" width="9" height="66"/><rect x="142" y="64" width="9" height="48"/><rect x="161" y="56" width="9" height="56"/><rect x="180" y="74" width="9" height="38"/><rect x="199" y="60" width="9" height="52"/><rect x="218" y="66" width="9" height="46"/><rect x="237" y="58" width="9" height="54"/></g>
        <g fill="var(--bar-dark)"><rect x="28" y="80" width="9" height="32"/><rect x="47" y="86" width="9" height="26"/><rect x="66" y="88" width="9" height="24"/><rect x="85" y="72" width="9" height="40"/><rect x="104" y="76" width="9" height="36"/><rect x="123" y="82" width="9" height="30"/><rect x="142" y="88" width="9" height="24"/><rect x="161" y="86" width="9" height="26"/><rect x="180" y="92" width="9" height="20"/><rect x="199" y="88" width="9" height="24"/><rect x="218" y="90" width="9" height="22"/><rect x="237" y="86" width="9" height="26"/></g>
      </svg>
    </div>

    <div class="chart" style="left:44px;top:290px">
      <div class="chart-title">Lorem ipsum</div>
      <div class="chart-note">Lorem ipsum dolor sit amet, consectetur adipiscing elit</div>
      <svg viewBox="0 0 258 118">
        <g fill="var(--muted)" font-size="6" font-family="Arimo, sans-serif"><text x="0" y="10">140</text><text x="0" y="40">100</text><text x="4" y="70">60</text><text x="4" y="100">20</text></g>
        <line x1="20" y1="112" x2="255" y2="112" stroke="var(--axis)"/>
        <g fill="var(--bar-light)"><rect x="28" y="56" width="9" height="56"/><rect x="47" y="52" width="9" height="60"/><rect x="66" y="44" width="9" height="68"/><rect x="85" y="62" width="9" height="50"/><rect x="104" y="66" width="9" height="46"/><rect x="123" y="70" width="9" height="42"/><rect x="142" y="62" width="9" height="50"/><rect x="161" y="66" width="9" height="46"/><rect x="180" y="68" width="9" height="44"/><rect x="199" y="64" width="9" height="48"/><rect x="218" y="56" width="9" height="56"/><rect x="237" y="64" width="9" height="48"/></g>
        <g fill="var(--bar-dark)"><rect x="28" y="84" width="9" height="28"/><rect x="47" y="82" width="9" height="30"/><rect x="66" y="80" width="9" height="32"/><rect x="85" y="86" width="9" height="26"/><rect x="104" y="88" width="9" height="24"/><rect x="123" y="90" width="9" height="22"/><rect x="142" y="84" width="9" height="28"/><rect x="161" y="88" width="9" height="24"/><rect x="180" y="88" width="9" height="24"/><rect x="199" y="86" width="9" height="26"/><rect x="218" y="84" width="9" height="28"/><rect x="237" y="86" width="9" height="26"/></g>
      </svg>
    </div>

    <div class="chart" style="left:300px;top:290px">
      <div class="chart-title">Lorem ipsum</div>
      <div class="chart-note">Lorem ipsum dolor sit amet, consectetur adipiscing elit</div>
      <svg viewBox="0 0 258 118">
        <g fill="var(--muted)" font-size="6" font-family="Arimo, sans-serif"><text x="0" y="10">140</text><text x="0" y="40">100</text><text x="4" y="70">60</text><text x="4" y="100">20</text></g>
        <line x1="20" y1="112" x2="255" y2="112" stroke="var(--axis)"/>
        <g fill="var(--bar-light)"><rect x="28" y="62" width="9" height="50"/><rect x="47" y="50" width="9" height="62"/><rect x="66" y="36" width="9" height="76"/><rect x="85" y="28" width="9" height="84"/><rect x="104" y="38" width="9" height="74"/><rect x="123" y="56" width="9" height="56"/><rect x="142" y="28" width="9" height="84"/><rect x="161" y="30" width="9" height="82"/><rect x="180" y="58" width="9" height="54"/><rect x="199" y="44" width="9" height="68"/><rect x="218" y="42" width="9" height="70"/></g>
        <g fill="var(--bar-dark)"><rect x="28" y="84" width="9" height="28"/><rect x="47" y="80" width="9" height="32"/><rect x="66" y="74" width="9" height="38"/><rect x="85" y="70" width="9" height="42"/><rect x="104" y="74" width="9" height="38"/><rect x="123" y="82" width="9" height="30"/><rect x="142" y="70" width="9" height="42"/><rect x="161" y="72" width="9" height="40"/><rect x="180" y="82" width="9" height="30"/><rect x="199" y="76" width="9" height="36"/><rect x="218" y="74" width="9" height="38"/></g>
      </svg>
    </div>

    <div class="legend"><span class="light">Text</span><br><span class="dark">Text</span></div>

    <div class="notes">
      <p class="note">Lorem ipsum dolor sit amet, consetetur sadipscing elitr, sed diam nonumy eirmod tempor invidunt ut labore et dolore magna aliquyam erat, sed diam voluptua. At vero eos et accusam.</p>
      <p class="note">Lorem ipsum dolor sit amet, consetetur sadipscing elitr, sed diam nonumy eirmod tempor invidunt ut labore et dolore magna aliquyam erat, sed diam voluptua. At vero eos et accusam.</p>
      <p class="note">Lorem ipsum dolor sit amet, consetetur sadipscing elitr, sed diam nonumy eirmod tempor invidunt ut labore et dolore magna aliquyam erat, sed diam voluptua. At vero eos et accusam.</p>
    </div>
  </div>

  <p class="caption">SLIDEDECK TEMPLATE 1</p>
</div>
</body>
</html>
```